Namecard Designs+Logo for a High End Automobile Company

We need a new business card for our company called Velta Motorhof.

www.veltamotorhof.example.sg
Our new website will be up in 2.5 months time.

We sell used and brand new continental cars like Korvane, QTL, Dravell, Solbrini and etc. Currently we are operating from 2 offices in Singapore and United Kingdom.

We want a design which is serious. We are open to colours but try to keep it at a maximum of 3 colours.

We prefer something simple and minimal. We are open to 2 sides printing or even 2 sided namecards. Both UK and Singapore company offices address must be in; either side by side, front and back, or even 2 sided cards.

The logo can be a text logo, emblem, abstract, pictorial or combination.

We are printing with Pribo.com so please kindly follow the printing guideline.

http://uk.pribo.example/help/faq/templates-and-guidelines.html

Rich and Car Enthusiasts

Printing

Must have
• Our 2 offices; UK and Singapore.

Our slogan which is " The Automobile Specialist"
Should not have
• Not more than 3 colours

```html
<!DOCTYPE html>
<html lang="en">
<head>
<meta charset="utf-8">
<title>Velta Motorhof – Business Card</title>
<link rel="stylesheet" href="https://fonts.googleapis.com/css2?family=Tinos:wght@400;700&display=swap">
<style>
  :root {
    --stage: #dcdcdc;
    --card-black: #000000;
    --panel-light: #ffffff;
    --panel-grey: #8c8c8c;
    --accent-red: #e3000f;
    --text-white: #ffffff;
    --emblem-fill: #2b2b2b;
    --car-dark: #1c1c1c;
    --car-mid: #6a6a6a;
  }
  * { margin: 0; padding: 0; box-sizing: border-box; }
  html, body {
    width: 1200px;
    height: 945px;
    overflow: hidden;
    background: var(--stage);
    font-family: "Tinos", "Times New Roman", serif;
  }
  .business-card {
    position: absolute;
    left: 100px;
    top: 154px;
    width: 1000px;
    height: 636px;
    background: var(--card-black);
    overflow: hidden;
  }
  .showroom-panel {
    position: absolute;
    left: 0;
    top: 0;
    width: 480px;
    height: 100%;
    background: linear-gradient(180deg, var(--panel-grey) 0%, #cfcfcf 55%, var(--panel-light) 100%);
  }
  .car-visual {
    position: absolute;
    left: 8px;
    top: 164px;
    width: 400px;
    height: 300px;
    background: linear-gradient(180deg, var(--car-dark) 0%, var(--car-dark) 58%, var(--car-mid) 62%, rgba(255,255,255,0) 100%);
    border-radius: 120px 90px 10px 10px / 70px 60px 10px 10px;
  }
  .brand-emblem {
    position: absolute;
    left: 350px;
    top: 78px;
    width: 260px;
    height: 260px;
  }
  .contact-name {
    position: absolute;
    left: 640px;
    top: 200px;
    color: var(--accent-red);
    font-size: 48px;
    line-height: 1;
    font-weight: 400;
  }
  .contact-role {
    position: absolute;
    left: 642px;
    top: 250px;
    color: var(--accent-red);
    font-size: 33px;
    line-height: 1;
  }
  .contact-phone {
    position: absolute;
    right: 36px;
    top: 292px;
    color: var(--text-white);
    font-size: 25px;
    line-height: 1;
  }
  .contact-phone .label { color: var(--accent-red); }
  .slogan {
    position: absolute;
    right: 36px;
    top: 332px;
    color: var(--text-white);
    font-size: 18px;
    line-height: 1;
    letter-spacing: 1px;
  }
  .office-list {
    position: absolute;
    left: 498px;
    top: 404px;
    color: var(--text-white);
    font-size: 21px;
    line-height: 28px;
  }
  .office + .office { margin-top: 10px; }
  .office-label { color: var(--accent-red); }
  .website {
    margin-top: 14px;
    color: var(--accent-red);
  }
</style>
</head>
<body>
  <main class="business-card">
    <div class="showroom-panel">
      <div class="car-visual" role="img" aria-label="Black sports car illustration with reflection on a light showroom floor"></div>
    </div>

    <svg class="brand-emblem" viewBox="0 0 260 260" aria-label="Velta Motorhof">
      <circle cx="130" cy="130" r="128" fill="var(--emblem-fill)"/>
      <text x="130" y="124" text-anchor="middle" fill="var(--text-white)" font-family="Tinos, 'Times New Roman', serif" font-size="30">VELTA</text>
      <text x="130" y="158" text-anchor="middle" fill="var(--text-white)" font-family="Tinos, 'Times New Roman', serif" font-size="30">MOTORHOF</text>
    </svg>

    <h1 class="contact-name">JOHN DOE</h1>
    <p class="contact-role">PROJECT MANAGER</p>
    <p class="contact-phone"><span class="label">PHONE</span>(999)-999-9999</p>
    <p class="slogan">THE AUTOMOBILE SPECIALIST</p>

    <div class="office-list">
      <div class="office">
        <p class="office-label">UK ADDRESS:</p>
        <p>14 HARROW LANE, ASHBY HOUSE,</p>
        <p>LONDON EC2V 7QN</p>
      </div>
      <div class="office">
        <p class="office-label">SG ADDRESS:</p>
        <p>8 MARLOW QUAY, MARLOW POINT,</p>
        <p>#02-01 SINGAPORE 049877</p>
      </div>
      <p class="website">WWW.VELTAMOTORHOF.EXAMPLE.SG</p>
    </div>
  </main>
</body>
</html>
```